Packaging for Phone Case

I need help on packaging design for my new product, we are new, so it will be our first product.
. Phone Case
This case for all phone case, so just one size, the biggest one is for Brantis Slate 7. So the inner past as the holder of the case can be change accordingly. Here I upload the photo of the prodcut just to give some brief introductory. The theme is color full, most of the product have 6 colors, so I want something unique that can significantly represent my company.
Please fill free to contact me, i have the logo ready. Really appreciate your help. thanks
Target Market(s)
Youngster and the gadget junkiest.
Industry/Entity Type
It Company
Look and feel
Each slider illustrates characteristics of the customer's brand and the style your logo design should communicate.

```html
<!DOCTYPE html>
<html lang="en">
<head>
<meta charset="utf-8">
<title>Velio Phone Case Packaging Dieline</title>
<link rel="stylesheet" href="https://fonts.googleapis.com/css2?family=Anton&family=Open+Sans:wght@700&display=swap">
<style>
  :root {
    --paper: #ffffff;
    --cut-line: #6d6d6d;
    --window: #e6e7e8;
    --ink: #111111;
    --plum: #8a3d7c;
    --magenta: #e5306a;
    --coral: #f26a4b;
    --orange: #f39a3a;
    --slate: #7b7a86;
  }
  html, body {
    margin: 0;
    padding: 0;
    width: 1200px;
    height: 1106px;
    overflow: hidden;
    background: var(--paper);
  }
  .dieline {
    display: block;
    width: 1200px;
    height: 1106px;
  }
  .cut { fill: none; stroke: var(--cut-line); stroke-width: 1; }
  .panel { fill: var(--paper); stroke: var(--cut-line); stroke-width: 1; }
  .window { fill: var(--window); }
  .title-band { fill: var(--paper); }
  .headline {
    font-family: "Anton", sans-serif;
    font-size: 52px;
    fill: var(--ink);
  }
  .tagline {
    font-family: "Open Sans", sans-serif;
    font-weight: 700;
    font-size: 19px;
    fill: var(--ink);
  }
  .brand-name {
    font-family: "Anton", sans-serif;
    font-size: 30px;
    fill: var(--paper);
  }
  .side-brand {
    font-family: "Anton", sans-serif;
    font-size: 20px;
    fill: var(--ink);
  }
  .side-title {
    font-family: "Anton", sans-serif;
    font-size: 44px;
    fill: var(--paper);
    stroke: var(--ink);
    stroke-width: 1.2;
  }
</style>
</head>
<body>
<svg class="dieline" viewBox="0 0 1080 995" xmlns="http://www.w3.org/2000/svg">
  <defs>
    <linearGradient id="front-wash" x1="0" y1="0" x2="1" y2="1">
      <stop offset="0" stop-color="#c04c86"/>
      <stop offset="0.3" stop-color="#e5306a"/>
      <stop offset="0.55" stop-color="#f27b4f"/>
      <stop offset="0.8" stop-color="#a85a96"/>
      <stop offset="1" stop-color="#f0a27c"/>
    </linearGradient>
    <linearGradient id="flap-wash" x1="0" y1="0" x2="0" y2="1">
      <stop offset="0" stop-color="#b27aa6" stop-opacity="0.85"/>
      <stop offset="0.55" stop-color="#d9a07a" stop-opacity="0.45"/>
      <stop offset="1" stop-color="#ffffff" stop-opacity="0"/>
    </linearGradient>
    <linearGradient id="left-side-wash" x1="0" y1="0" x2="0" y2="1">
      <stop offset="0" stop-color="#a05a92" stop-opacity="0.8"/>
      <stop offset="0.35" stop-color="#f0a050" stop-opacity="0.7"/>
      <stop offset="0.7" stop-color="#a38aa6" stop-opacity="0.55"/>
      <stop offset="1" stop-color="#ffffff" stop-opacity="0"/>
    </linearGradient>
    <linearGradient id="right-side-wash" x1="0" y1="0" x2="0" y2="1">
      <stop offset="0" stop-color="#ffffff" stop-opacity="0"/>
      <stop offset="0.25" stop-color="#a38aa6" stop-opacity="0.6"/>
      <stop offset="0.6" stop-color="#f0a050" stop-opacity="0.75"/>
      <stop offset="1" stop-color="#8a3d7c" stop-opacity="0.8"/>
    </linearGradient>
  </defs>

  <!-- Front panel -->
  <g class="front-panel">
    <path d="M136 860 V190 Q136 160 166 160 H442 Q472 160 472 190 V860 Z"
          fill="url(#front-wash)" stroke="var(--cut-line)" stroke-width="1"
          role="img" aria-label="Watercolour artwork in plum, magenta, coral and orange"/>
    <line class="cut" x1="136" y1="203" x2="472" y2="203"/>
    <line class="cut" x1="136" y1="248" x2="472" y2="248"/>
    <text class="brand-name" x="304" y="312" text-anchor="middle">Velio</text>
    <rect class="window" x="172" y="360" width="268" height="422" rx="22"/>
    <polygon class="title-band" points="172,640 472,588 472,700 172,752"/>
    <g transform="rotate(-11 175 712)">
      <text class="headline" x="175" y="712" textLength="262" lengthAdjust="spacingAndGlyphs">PHONE CASE</text>
      <text class="tagline" x="205" y="737" textLength="200" lengthAdjust="spacingAndGlyphs">for your smartphone</text>
    </g>
  </g>

  <!-- Back, sides and flaps -->
  <g class="back-structure">
    <rect class="panel" x="532" y="45" width="338" height="117"/>
    <rect class="panel" x="532" y="162" width="338" height="96"/>
    <rect class="panel" x="532" y="258" width="338" height="602"/>
    <rect class="panel" x="475" y="258" width="57" height="602"/>
    <rect class="panel" x="870" y="258" width="58" height="602"/>
    <path class="panel" d="M928 258 H940 Q948 258 948 266 V852 Q948 860 940 860 H928 Z"/>
    <path class="panel" d="M475 258 V230 L486 218 H521 L532 230 V258 Z"/>
    <path class="panel" d="M870 258 V230 L881 218 H917 L928 230 V258 Z"/>
    <path class="panel" d="M475 860 V888 L486 898 H521 L532 888 V860 Z"/>
    <path class="panel" d="M870 860 V888 L881 898 H917 L928 888 V860 Z"/>
    <rect class="panel" x="532" y="860" width="338" height="55"/>
    <path class="panel" d="M532 915 V935 Q532 955 552 955 H850 Q870 955 870 935 V915 Z"/>

    <rect x="532.5" y="45.5" width="337" height="116" fill="url(#flap-wash)"
          role="img" aria-label="Watercolour artwork in plum and orange"/>
    <rect x="475.5" y="258.5" width="56" height="360" fill="url(#left-side-wash)"
          role="img" aria-label="Watercolour artwork in plum, orange and grey"/>
    <rect x="870.5" y="480" width="77" height="379.5" fill="url(#right-side-wash)"
          role="img" aria-label="Watercolour artwork in grey, orange and plum"/>

    <rect class="cut" x="645" y="104" width="112" height="22" rx="11"/>
    <rect class="cut" x="645" y="198" width="112" height="22" rx="11"/>

    <g class="side-left">
      <text class="side-brand" transform="translate(511 340) rotate(-90)" text-anchor="middle">Velio</text>
      <text class="side-title" transform="translate(520 665) rotate(-90)" textLength="215" lengthAdjust="spacingAndGlyphs">PHONE CASE</text>
      <text class="side-brand" transform="translate(511 775) rotate(-90)" text-anchor="middle">Velio</text>
    </g>
    <g class="side-right">
      <text class="side-brand" transform="translate(906 340) rotate(-90)" text-anchor="middle">Velio</text>
      <text class="side-title" transform="translate(916 665) rotate(-90)" textLength="215" lengthAdjust="spacingAndGlyphs">PHONE CASE</text>
      <text class="side-brand" transform="translate(906 775) rotate(-90)" text-anchor="middle">Velio</text>
    </g>
  </g>
</svg>
</body>
</html>
```